Business Card for Managing Partner Investment Fund

To create a business card template for an investment fund manager. Business card should be more professional in nature, not too colorful, more upscale, and created using the attached logos and fund name files. I would prefer a black or gray color scheme, but am open to the use of color as well. I would prefer a double sided business card, but open to single sided business card designs as well. The business card should include: name, title, and contact information, as well as logo and company name. I would prefer a more stream-lined, simple business card design.
Updates
Address: 4136 NE 19th Ter. Ocala, FL 34470
Email: travis48@quillnet-mail.com
Phone: 561-374-9186
Title: managing partner
Name: Travis Whitlow
Fund Name: Emberfall Capital
Logos can be found in files attached to the brief
Target Market(s)
potential investors, other fund managers
Industry/Entity Type
Finance
Contact Information for Business Card
Name on card: Travis Whitlow
Title: Managing Partner
Font styles to use
Colors
Designer to choose colors to be used in the design.
Requirements
Must have
- Phone number
- email address
- physical address
- title
- name
- logo
- Fund name
Nice to have
- simple layout
Should not have
- too many colors, busy fonts,

```html
<!DOCTYPE html>
<html lang="en">
<head>
<meta charset="utf-8">
<title>Emberfall Capital — Business Card</title>
<link href="https://fonts.googleapis.com/css2?family=Cinzel:wght@400;600&family=Tinos&display=swap" rel="stylesheet">
<style>
  :root {
    --stage: #2b2b2b;
    --card-dark: #3b3b3b;
    --card-light: #ffffff;
    --ink: #111111;
    --ink-soft: #6d6d6d;
    --paper-text: #ffffff;
    --peak-dark: #101010;
    --peak-mid: #6a6a6a;
    --peak-light: #d9d9d9;
  }
  * { box-sizing: border-box; margin: 0; padding: 0; }
  html, body {
    width: 1200px; height: 880px; overflow: hidden;
    background: var(--stage);
  }
  .canvas {
    position: relative; width: 1200px; height: 880px;
  }
  .card {
    position: absolute; width: 660px; height: 377px;
    overflow: hidden;
    box-shadow: 0 10px 30px rgba(0,0,0,.45);
  }
  /* Front side */
  .card--front { left: 270px; top: 36px; background: var(--card-dark); }
  .card--front .brand {
    position: absolute; left: 54px; top: 128px;
    font-family: "Cinzel", serif; font-weight: 600;
    font-size: 34px; letter-spacing: 2px;
    color: var(--paper-text);
  }
  .card--front .peak-art {
    position: absolute; right: 0; bottom: 0;
    width: 330px; height: 300px;
    clip-path: polygon(100% 0, 100% 100%, 0 100%);
    background: linear-gradient(200deg, var(--peak-light) 0%, var(--peak-mid) 45%, #2a2a2a 100%);
  }
  /* Back side */
  .card--back { left: 270px; top: 453px; background: var(--card-light); }
  .card--back .brand {
    position: absolute; right: 40px; top: 42px;
    font-family: "Cinzel", serif; font-weight: 600;
    font-size: 28px; letter-spacing: 2px;
    color: var(--ink);
  }
  .contact {
    position: absolute; left: 44px; top: 150px;
    font-family: "Tinos", serif; color: var(--ink);
  }
  .contact__name {
    font-family: "Cinzel", serif; font-weight: 600;
    font-size: 21px; letter-spacing: 1px;
  }
  .contact__title {
    font-size: 15px; color: var(--ink-soft); margin-bottom: 16px;
  }
  .contact__line { font-size: 15px; line-height: 20px; }
  .contact__row {
    display: flex; align-items: center; gap: 8px;
    font-size: 15px; line-height: 22px; margin-left: 18px;
  }
  .contact__address { margin-left: 18px; margin-bottom: 4px; }
  .icon {
    width: 16px; height: 16px; flex: none;
  }
  .card--back .peak-art {
    position: absolute; right: 0; bottom: 0;
    width: 340px; height: 250px;
    clip-path: polygon(100% 0, 100% 100%, 0 100%);
    background: linear-gradient(160deg, var(--peak-dark) 0%, #4a4a4a 55%, var(--peak-light) 100%);
  }
</style>
</head>
<body>
<main class="canvas">

  <section class="card card--front" aria-label="Card front">
    <div class="brand">Emberfall Capital</div>
    <div class="peak-art" role="img" aria-label="Large silver mountain peaks decoration"></div>
  </section>

  <section class="card card--back" aria-label="Card back">
    <div class="brand">Emberfall Capital</div>

    <div class="contact">
      <p class="contact__name">Travis Whitlow</p>
      <p class="contact__title">Managing Partner</p>
      <div class="contact__address">
        <p class="contact__line">4136 NE 19th Ter.</p>
        <p class="contact__line">Ocala, FL 34470</p>
      </div>
      <p class="contact__row">
        <svg class="icon" viewBox="0 0 16 16" aria-hidden="true">
          <rect width="16" height="16" fill="#6d6d6d"/>
          <path d="M4 4.5c0 4 3.5 7.5 7.5 7.5l1-1.8-2-1.2-1 1c-1.4-.6-2.4-1.6-3-3l1-1-1.2-2z" fill="#fff"/>
        </svg>
        561-374-9186
      </p>
      <p class="contact__row">
        <svg class="icon" viewBox="0 0 16 16" aria-hidden="true">
          <rect width="16" height="16" fill="#6d6d6d"/>
          <rect x="3" y="4.5" width="10" height="7" fill="none" stroke="#fff" stroke-width="1.2"/>
          <path d="M3 4.5l5 4 5-4" fill="none" stroke="#fff" stroke-width="1.2"/>
        </svg>
        travis48@quillnet-mail.com
      </p>
    </div>

    <div class="peak-art" role="img" aria-label="Large black and white mountain peaks decoration"></div>
  </section>

</main>
</body>
</html>
```